Business Cards for Veltrin Massage and Wellness

I worked with designers from Pixel Harbor to make a wonderful logo and now I would like to use it in a business card. I have an intimate but progressive small clinical massage practice with far infrared sauna therapy for detox, vitadraw for pre and post surgery healing and ashiatsu and sports massage. We do lots of different modalities and I would like each therapist to have the same business card with their names on them. I would like to express our professionalism and connection to health.

I am attaching my logo and would like that included in the design. I love blues and greens. I would like something clean but creative, professional yet personality. I love the font copperplate gothic or I suppose whatever matches the logo. I would like to have the following information on the front of the card...

1. Logo

2. Address: Marlow Pavilion
2867 Tesslin Rd
Richmond, Va 23228
3. Phone: 804 519-2076

4. www.veltrinmassageandwellness.example

5. name of therapist, CMT (for example purposes Corin Mathers, CMT)

6. Optional information for front of card....
Far Infrared Sauna, Neuromuscular Therapy, VitaDraw, Detox Program, Deep Tissue, Swedish, Ashiatsu, Craniosacral Therapy, Reiki, Sports Massage, Couples Massage, Hot Stones, Cold Stones, LED Light Therapy

back of card...

1. Appointment Date/Time

2. Please provide 24 hours notice of cancellations

3. a line or space for appointment times.

```html
<!DOCTYPE html>
<html lang="en">
<head>
<meta charset="utf-8">
<title>Veltrin Massage and Wellness – Business Card</title>
<link rel="stylesheet" href="https://fonts.googleapis.com/css2?family=Delius&display=swap">
<style>
  :root {
    --bg-start: #c9c5d9;
    --bg-mid: #ddd3dc;
    --bg-end: #f8e2d1;
    --brand-gold: #a3956a;
    --brand-teal: #5f9f9c;
    --mark-teal: #86b8ab;
    --ink: #4c5a55;
    --rule: #6e6a6a;
    --frame-blue: #7b84bd;
  }
  * { margin: 0; padding: 0; box-sizing: border-box; }
  html, body { width: 1200px; height: 792px; overflow: hidden; }
  body { font-family: "Delius", "Comic Sans MS", cursive; color: var(--ink); }

  .card {
    position: relative;
    width: 1200px;
    height: 792px;
    background: linear-gradient(120deg, var(--bg-start) 0%, var(--bg-mid) 45%, var(--bg-end) 100%);
    overflow: hidden;
  }

  .brand-mark {
    position: absolute;
    left: 40px; top: 36px;
    width: 262px; height: 262px;
    border-radius: 50%;
    background: var(--mark-teal);
  }
  .brand-name {
    position: absolute;
    left: 318px; top: 110px;
    width: 640px;
    font-size: 46px;
    font-weight: 400;
    line-height: 1;
    white-space: nowrap;
    color: var(--brand-gold);
  }
  .tagline {
    position: absolute;
    left: 318px; top: 218px;
    width: 634px;
    padding-top: 6px;
    border-top: 2px solid var(--brand-teal);
    font-size: 22px;
    white-space: nowrap;
    color: var(--brand-teal);
  }

  .address {
    position: absolute;
    left: 40px; top: 308px;
    width: 620px;
    text-align: center;
    font-size: 38px;
    line-height: 69px;
    font-style: normal;
  }
  .address-rule {
    position: absolute;
    left: 81px; top: 543px;
    width: 531px; height: 2px;
    background: var(--rule);
  }
  .phone {
    position: absolute;
    left: 46px; top: 600px;
    font-size: 38px;
  }
  .divider {
    position: absolute;
    left: 733px; top: 323px;
    width: 2px; height: 280px;
    background: var(--rule);
  }

  .therapist {
    position: absolute;
    left: 771px; top: 286px;
    width: 320px; height: 126px;
  }
  .therapist svg { position: absolute; inset: 0; }
  .therapist-name {
    position: relative;
    text-align: center;
    font-size: 36px;
    line-height: 56px;
    padding-top: 8px;
  }

  .services {
    position: absolute;
    left: 731px; top: 425px;
    width: 440px;
    list-style: none;
    text-align: center;
    font-size: 34px;
    line-height: 75px;
    white-space: nowrap;
  }
  .services-etc {
    position: absolute;
    left: 1008px; top: 664px;
    font-size: 34px;
  }

  .website {
    position: absolute;
    left: 0; top: 692px;
    width: 1142px;
    text-align: center;
    font-size: 36px;
    white-space: nowrap;
  }
</style>
</head>
<body>
  <main class="card">
    <div class="brand-mark" aria-hidden="true"></div>
    <h1 class="brand-name">Veltrin Massage and Wellness</h1>
    <p class="tagline">Promoting Preventative Care And Post-surgery Healing</p>

    <address class="address">
      Address: Marlow Pavilion<br>
      2867 Tesslin Rd<br>
      Richmond, Va 23228
    </address>
    <div class="address-rule"></div>
    <p class="phone">Phone: 804 519-2076</p>

    <div class="divider"></div>

    <div class="therapist">
      <svg width="320" height="126" viewBox="0 0 320 126" aria-hidden="true">
        <path d="M8 8 Q80 2 160 7 T312 6 Q318 60 313 119 Q240 124 160 118 T7 120 Q3 64 8 8 Z"
              fill="none" stroke="var(--frame-blue)" stroke-width="7" stroke-linejoin="round"/>
      </svg>
      <p class="therapist-name">Corin Mathers<br>CMT</p>
    </div>

    <ul class="services">
      <li>Neuromuscular Theraphy,</li>
      <li>Sport Massages,</li>
      <li>Couple Massages,</li>
    </ul>
    <p class="services-etc">etc.</p>

    <p class="website">www.veltrinmassageandwellness.example</p>
  </main>
</body>
</html>
```